A weight loss and fitness website design

I am into different types of modern weight loss techniques for people who are a little fatty and wish to be physically and mentally fit. Basically, the website is to teach people how to reduce weight using different methods such as diet, exercises, yoga and other forms. I would need an eye catching website which would make visitors want to come back. The will be also be different forms of exercises for a health and fit life. This said, my website is to have two categories of
1) weight loss techniques
2) exercise of fit and healthy living.
I prefer bright colors such as green, blue, yellow, and orange. Imagery should include before and after pictures of people suffering from obesity, people under going exercises.
Designers can get ideas and inspiration from the website fyrnexa.com which i was previously part of the team.
Target Market(s)
My target audience are people suffering from obesity, malnutrition and physical deficiency.
Industry/Entity Type
Fitness
Coding
Number of Pages Required
1 page
Look and feel

```html
<!DOCTYPE html>
<html lang="en">
<head>
<meta charset="utf-8">
<title>Valora Weight Loss Studio</title>
<link href="https://fonts.googleapis.com/css2?family=Montserrat:wght@400;600;700;800&family=Playfair+Display:ital@1&display=swap" rel="stylesheet">
<style>
:root{
  --blue:#2f87e2;
  --green:#3ba53a;
  --red:#e0334c;
  --dark:#262626;
  --grey:#efefef;
  --text:#555;
  --white:#fff;
}
*{margin:0;padding:0;box-sizing:border-box}
html,body{width:1200px;height:4119px;overflow:hidden}
body{position:relative;background:var(--white);font-family:'Montserrat',sans-serif;color:var(--text)}
.abs{position:absolute}
.script{font-family:'Playfair Display',serif;font-style:italic}

/* hero */
.hero{left:0;top:0;width:1200px;height:610px;background:linear-gradient(180deg,#3a3632 0%,#2a2724 55%,#4a443e 100%)}
.nav{right:60px;top:86px;display:flex;gap:26px;font-size:13px;font-weight:700;color:var(--white);letter-spacing:.5px}
.top-icons{right:60px;top:36px;display:flex;gap:18px}
.hero-brand{left:0;width:1200px;top:178px;text-align:center;color:var(--white);font-size:30px}
.hero-title{left:0;width:1200px;top:242px;text-align:center;color:var(--white);font-size:38px;font-weight:700;letter-spacing:1px}
.hero-sub{left:0;width:1200px;top:300px;text-align:center;color:var(--white);font-size:14px;font-weight:700;letter-spacing:.5px}
.arrow{top:266px;color:var(--white);font-size:34px}
.dots{right:24px;top:540px;display:flex;flex-direction:column;gap:8px}
.dots span{width:9px;height:9px;border:2px solid var(--white);border-radius:50%}

/* info boxes */
.card{background:var(--blue);color:var(--white);font-size:13px;font-weight:600}
.card h3{font-size:15px;font-weight:700;text-align:center;letter-spacing:.5px}
.card .rule{height:1px;background:rgba(255,255,255,.5);margin:18px 24px}
.hours{left:80px;top:582px;width:326px;height:379px;padding-top:28px}
.hours li{list-style:none;display:flex;align-items:center;gap:14px;margin:0 0 15px 40px}
.next{left:437px;top:420px;width:326px;height:541px}
.next h3{padding:24px 0 22px}
.next-photo{width:326px;height:165px;background:linear-gradient(135deg,#5b524a,#2b2623)}
.next ul{padding:22px 0 0 40px}
.next li{list-style:none;display:flex;gap:16px;margin-bottom:20px;line-height:1.5}
.contact{left:794px;top:582px;width:326px;height:379px;padding-top:28px}
.contact li{list-style:none;display:flex;gap:16px;margin:0 0 24px 50px;line-height:1.55}
.dash{width:0;height:82px;border-left:2px dashed #bbb;top:961px}
.btn-out{border:3px solid var(--green);color:var(--green);border-radius:30px;font-size:13px;font-weight:700;text-align:center;line-height:44px;height:50px;width:182px;top:1049px;letter-spacing:.5px}

/* headings */
.kicker{left:0;width:1200px;text-align:center;font-size:15px;color:#666}
.heading{left:0;width:1200px;text-align:center;font-size:27px;font-weight:800;color:#333;letter-spacing:1px}
.divider{left:580px;width:40px}

/* about */
.devices{left:66px;top:1337px;width:519px;height:486px;background:linear-gradient(160deg,#4a4440,#1f1d1c);border-radius:26px 26px 0 0}
.feature{left:620px;width:520px}
.feature h4{position:absolute;left:124px;top:0;color:var(--blue);font-size:14px;font-weight:700}
.feature p{position:absolute;left:124px;top:26px;width:400px;font-size:13px;line-height:1.6;color:#666}

/* stats */
.stats{left:0;top:1823px;width:1200px;height:442px;background:var(--grey)}
.tile{top:1919px;width:290px;height:253px;background:linear-gradient(135deg,#3d3732,#17150f);clip-path:polygon(130px 0,100% 0,100% 100%,0 100%)}
.tile .num{position:absolute;right:40px;top:20px;font-size:76px;color:var(--blue)}
.tile .lbl{position:absolute;right:40px;top:140px;text-align:right;color:var(--white);font-size:28px;font-weight:800;line-height:1.05}
.slash{width:2px;height:330px;background:#333;transform:rotate(24deg);top:1870px}

/* join */
.promo{left:0;top:2265px;width:1200px;height:325px;background:linear-gradient(90deg,#2b2724,#4a443f 50%,#2b2724)}
.promo-kicker{left:0;width:1200px;top:2340px;text-align:center;color:var(--white);font-size:32px}
.promo-title{left:0;width:1200px;top:2397px;text-align:center;color:var(--white);font-size:40px;font-weight:800;letter-spacing:1px}
.btn-white{left:515px;top:2470px;width:170px;height:46px;border:3px solid var(--white);border-radius:30px;color:var(--white);font-size:13px;font-weight:700;text-align:center;line-height:40px}

/* classes */
.class-band{left:0;top:2878px;width:1200px;height:340px;background:linear-gradient(90deg,#5a4e4c,#9c8a86 45%,#3d3433)}
.class-nums{left:85px;top:2806px;width:159px;height:467px;background:#444;color:var(--white);text-align:center}
.class-nums span{display:block;font-size:22px;margin-top:18px}
.class-nums .big{font-size:58px;margin-top:14px}
.class-text{left:244px;top:2806px;width:437px;height:330px;background:rgba(238,238,238,.95);padding:44px 46px}
.class-text h4{font-size:14px;font-weight:700;color:#444;margin-bottom:14px}
.class-text p{font-size:13px;line-height:1.6;color:#777}
.class-text .btn-out{position:static;margin-top:18px;width:176px;height:46px;line-height:40px}
.class-info{left:928px;top:2806px;width:253px;height:198px;padding:22px 0 0 22px}
.class-info li{list-style:none;display:flex;gap:14px;align-items:center;margin-bottom:18px}

/* contact */
.map{left:0;top:3542px;width:1200px;height:377px;background:linear-gradient(90deg,#a9cdf5 0%,#b5d3f2 12%,#e6e1d3 14%,#ebe6d8 60%,#e4e8d8 100%)}
.form{left:66px;top:3487px;width:338px;height:486px;background:var(--blue);padding:26px 28px;z-index:2}
.form .field{background:var(--white);height:50px;margin-bottom:14px;padding:0 14px;font-family:'Playfair Display',serif;font-style:italic;font-size:13px;color:#aaa;line-height:50px}
.form .msg{height:170px;line-height:1;padding-top:14px}
.form .send{background:var(--white);height:44px;text-align:center;line-height:44px;font-size:13px;font-weight:700;color:#333;letter-spacing:1px;margin-top:10px}

/* footer */
.footer{left:0;top:3919px;width:1200px;height:200px;background:var(--dark)}
.social{left:496px;top:3988px;display:flex;gap:12px}
.social span{width:36px;height:36px;border:2px solid var(--white);border-radius:50%}
.copy{left:0;width:1200px;top:4052px;text-align:center;color:#ccc;font-size:13px}
</style>
</head>
<body>

<!-- hero -->
<div class="abs hero" role="img" aria-label="People exercising in a bright gym with weights and mats"></div>
<div class="abs top-icons">
  <svg width="22" height="22" viewBox="0 0 22 22" fill="none" stroke="#fff" stroke-width="1.6"><circle cx="11" cy="11" r="9"/><path d="M2 11h18M11 2c3 3 3 15 0 18M11 2c-3 3-3 15 0 18"/></svg>
  <svg width="22" height="22" viewBox="0 0 22 22" fill="none" stroke="#fff" stroke-width="1.6"><path d="M4 7h14l-1 13H5z"/><path d="M8 7V5a3 3 0 0 1 6 0v2"/></svg>
</div>
<nav class="abs nav"><span>HOME</span><span>ABOUT ▾</span><span>WEIGHT LOSS</span><span>TRAINERS</span><span>BLOG ▾</span><span>SHOP</span><span>CONTACT</span><span>PAGES ▾</span></nav>
<div class="abs hero-brand script">Valora</div>
<h1 class="abs hero-title">WEIGHT LOSS STUDIO</h1>
<div class="abs hero-sub">DIET / YOGA / CARDIO / FITNESS / AEROBICS / HEALTHY LIVING</div>
<div class="abs arrow" style="left:26px">‹</div>
<div class="abs arrow" style="right:26px">›</div>
<div class="abs dots"><span></span><span></span><span></span></div>

<!-- working hours -->
<section class="abs card hours">
  <h3>WORKING HOURS</h3>
  <div class="rule"></div>
  <ul>
    <li><svg width="20" height="20" viewBox="0 0 20 20" fill="none" stroke="#fff" stroke-width="1.5"><circle cx="10" cy="10" r="8.5"/><path d="M10 5v5l3 2"/></svg>Monday 9.00 - 17.00</li>
    <li><svg width="20" height="20" viewBox="0 0 20 20" fill="none" stroke="#fff" stroke-width="1.5"><circle cx="10" cy="10" r="8.5"/><path d="M10 5v5l3 2"/></svg>Tuesday 9.00 - 20.00</li>
    <li><svg width="20" height="20" viewBox="0 0 20 20" fill="none" stroke="#fff" stroke-width="1.5"><circle cx="10" cy="10" r="8.5"/><path d="M10 5v5l3 2"/></svg>Wednesday 9.00 - 20.00</li>
    <li><svg width="20" height="20" viewBox="0 0 20 20" fill="none" stroke="#fff" stroke-width="1.5"><circle cx="10" cy="10" r="8.5"/><path d="M10 5v5l3 2"/></svg>Thursday 9.00 - 20.00</li>
    <li><svg width="20" height="20" viewBox="0 0 20 20" fill="none" stroke="#fff" stroke-width="1.5"><circle cx="10" cy="10" r="8.5"/><path d="M10 5v5l3 2"/></svg>Friday 9.00 - 19.00</li>
    <li><svg width="20" height="20" viewBox="0 0 20 20" fill="none" stroke="#fff" stroke-width="1.5"><circle cx="10" cy="10" r="8.5"/><path d="M10 5v5l3 2"/></svg>Saturday 9.00 - 15.00</li>
    <li><svg width="20" height="20" viewBox="0 0 20 20" fill="none" stroke="#fff" stroke-width="1.5"><circle cx="10" cy="10" r="8.5"/><path d="M10 5v5l3 2"/></svg>Sunday 9.00 - 12.00</li>
  </ul>
</section>

<!-- what's next -->
<section class="abs card next">
  <h3>WHATS NEXT?</h3>
  <div class="next-photo" role="img" aria-label="Group exercise session on the gym floor"></div>
  <ul>
    <li><svg width="20" height="20" viewBox="0 0 20 20" fill="none" stroke="#fff" stroke-width="1.5"><rect x="2" y="4" width="16" height="14"/><path d="M2 8h16M6 2v4M14 2v4"/></svg><span>YOGA<br>Room C 9.00 - 10.00<br>Mira Holt</span></li>
    <li><svg width="20" height="20" viewBox="0 0 20 20" fill="none" stroke="#fff" stroke-width="1.5"><rect x="2" y="4" width="16" height="14"/><path d="M2 8h16M6 2v4M14 2v4"/></svg><span>DIET CLINIC<br>Room B 11.00 - 14.00<br>Lena Park</span></li>
    <li><svg width="20" height="20" viewBox="0 0 20 20" fill="none" stroke="#fff" stroke-width="1.5"><rect x="2" y="4" width="16" height="14"/><path d="M2 8h16M6 2v4M14 2v4"/></svg><span>CARDIO<br>Room A 16.00 - 18.00<br>Theo Varga</span></li>
  </ul>
</section>

<!-- contact info -->
<section class="abs card contact">
  <h3>CONTACT INFO</h3>
  <div class="rule"></div>
  <ul>
    <li><svg width="20" height="22" viewBox="0 0 20 22" fill="none" stroke="#fff" stroke-width="1.5"><path d="M10 20s-7-7-7-12a7 7 0 0 1 14 0c0 5-7 12-7 12z"/><circle cx="10" cy="8" r="2.5"/></svg><span>Alder Court<br>40218 PO 712 Brookfield<br>Northland</span></li>
    <li><svg width="20" height="20" viewBox="0 0 20 20" fill="none" stroke="#fff" stroke-width="1.5"><path d="M4 2h4l2 5-3 2a11 11 0 0 0 4 4l2-3 5 2v4a2 2 0 0 1-2 2A16 16 0 0 1 2 4a2 2 0 0 1 2-2z"/></svg><span>+ 555 014 232 19<br>+ 555 014 232 87</span></li>
    <li><svg width="20" height="20" viewBox="0 0 20 20" fill="none" stroke="#fff" stroke-width="1.5"><rect x="2" y="4" width="16" height="12"/><path d="M2 4l8 7 8-7"/></svg><span>hello@valorafit.com</span></li>
    <li><svg width="20" height="20" viewBox="0 0 20 20" fill="none" stroke="#fff" stroke-width="1.5"><rect x="2" y="3" width="16" height="14"/><path d="M2 7h16"/></svg><span>valora.fitness</span></li>
  </ul>
</section>

<div class="abs dash" style="left:243px"></div>
<div class="abs dash" style="left:600px"></div>
<div class="abs dash" style="left:957px"></div>
<div class="abs btn-out" style="left:153px">JOIN US</div>
<div class="abs btn-out" style="left:510px">VIEW TIMETABLE</div>
<div class="abs btn-out" style="left:867px">CONTACT US</div>

<!-- about -->
<div class="abs kicker script" style="top:1176px">A few words about us</div>
<h2 class="abs heading" style="top:1202px">GET TO KNOW US</h2>
<svg class="abs divider" style="top:1254px" height="14" viewBox="0 0 40 14" fill="none" stroke="#2f87e2" stroke-width="2"><path d="M4 2l8 10M12 2L4 12M16 2l8 10M24 2l-8 10M28 2l8 10M36 2l-8 10"/></svg>

<div class="abs devices" role="img" aria-label="Tablet and phone showing before and after weight loss results"></div>

<div class="abs feature" style="top:1340px">
  <svg class="abs" style="left:0;top:0" width="70" height="70" viewBox="0 0 70 70" fill="none" stroke="#e0334c" stroke-width="2.5"><circle cx="35" cy="14" r="7"/><path d="M35 22v20M18 36l17-8 17 8M12 56h46M22 50l13-8 13 8"/></svg>
  <h4>WEIGHT LOSS TECHNIQUES</h4>
  <p>Lose weight step by step with plans built around you: balanced diet, mindful eating, yoga and daily movement. Our coaches track your progress each week and adjust the plan so results last and your energy keeps rising.</p>
</div>
<div class="abs feature" style="top:1478px">
  <svg class="abs" style="left:0;top:0" width="70" height="70" viewBox="0 0 70 70" fill="none" stroke="#e0334c" stroke-width="2.5"><rect x="8" y="22" width="10" height="26"/><rect x="52" y="22" width="10" height="26"/><rect x="18" y="27" width="6" height="16"/><rect x="46" y="27" width="6" height="16"/><path d="M24 35h22M2 35h6M62 35h6"/></svg>
  <h4>EXERCISE FOR FIT LIVING</h4>
  <p>Strength, cardio and mobility sessions for every level, from first steps to full workouts. Build muscle, burn fat and protect your joints with guided exercise that fits into a busy week and keeps you moving.</p>
</div>
<div class="abs feature" style="top:1618px">
  <svg class="abs" style="left:0;top:0" width="70" height="70" viewBox="0 0 70 70" fill="none" stroke="#e0334c" stroke-width="2.5"><path d="M20 8c-8 4-14 14-12 26M50 8c8 4 14 14 12 26M20 8c5 6 25 6 30 0M24 20v40M46 20v40M24 34h22M24 46h22"/></svg>
  <h4>HEALTHY MIND AND BODY</h4>
  <p>Real change is physical and mental. Breathing, sleep and stress coaching sit next to your meal and training plans, so you feel calmer, stronger and more confident with every kilo you leave behind.</p>
</div>

<!-- stats -->
<div class="abs stats"></div>
<div class="abs tile" style="left:110px" role="img" aria-label="Training room with exercise equipment"><span class="num script">9</span><span class="lbl">TRAINING<br>ROOMS</span></div>
<div class="abs tile" style="left:480px" role="img" aria-label="Coach guiding a client through exercise"><span class="num script">18</span><span class="lbl">SKILLED<br>TRAINERS</span></div>
<div class="abs tile" style="left:845px" role="img" aria-label="Healthy meal plan on a table"><span class="num script">10</span><span class="lbl">DIET<br>PROGRAMS</span></div>
<div class="abs slash" style="left:140px"></div>
<div class="abs slash" style="left:510px"></div>
<div class="abs slash" style="left:875px"></div>

<!-- join -->
<div class="abs promo" role="img" aria-label="Person working out with a barbell"></div>
<div class="abs promo-kicker script">Ready to feel lighter and stronger?</div>
<h2 class="abs promo-title">START YOUR PLAN NOW</h2>
<div class="abs btn-white">GET STARTED</div>

<!-- classes -->
<div class="abs kicker script" style="top:2676px">Take a look at</div>
<h2 class="abs heading" style="top:2700px">OUR CLASSES</h2>
<svg class="abs" style="left:564px;top:2746px" width="72" height="16" viewBox="0 0 72 16" fill="none" stroke="#2f87e2" stroke-width="2"><path d="M8 2L2 8l6 6M64 2l6 6-6 6M20 3l8 10M28 3l-8 10M32 3l8 10M40 3l-8 10M44 3l8 10M52 3l-8 10"/></svg>

<div class="abs class-band" role="img" aria-label="Client doing a fat burning workout"></div>
<div class="abs class-nums script"><span>01</span><span class="big">02</span><span>03</span><span>04</span><span>05</span></div>
<div class="abs class-text">
  <h4>FAT BURN CIRCUIT</h4>
  <p>A low impact circuit made for people starting their weight loss journey. Short rounds of cardio and strength raise your heart rate safely, burn calories and build stamina. Every session ends with stretching and simple food tips to keep you on track between classes all week.</p>
  <div class="btn-out">VIEW TIMETABLE</div>
</div>
<ul class="abs card class-info">
  <li><svg width="20" height="20" viewBox="0 0 20 20" fill="none" stroke="#fff" stroke-width="1.5"><circle cx="10" cy="10" r="8.5"/><path d="M10 5v5l3 2"/></svg>Mon-Fri 9.00 - 10.00</li>
  <li><svg width="20" height="20" viewBox="0 0 20 20" fill="none" stroke="#fff" stroke-width="1.5"><circle cx="10" cy="10" r="8.5"/><circle cx="10" cy="8" r="3"/><path d="M4.5 16c2-3 9-3 11 0"/></svg>Nora Quill</li>
  <li><svg width="20" height="20" viewBox="0 0 20 20" fill="none" stroke="#fff" stroke-width="1.5"><circle cx="10" cy="10" r="8.5"/><path d="M6 14V7l4-2 4 2v7"/></svg>Room B</li>
  <li><svg width="20" height="20" viewBox="0 0 20 20" fill="none" stroke="#fff" stroke-width="1.5"><circle cx="10" cy="10" r="8.5"/><path d="M13 6.5c-1-1-6-1-6 1.5s6 1.5 6 4-5 2.5-6 1M10 4v12"/></svg>Starting with 100/mth</li>
</ul>

<!-- contact -->
<div class="abs kicker script" style="top:3381px">Get in touch with us</div>
<h2 class="abs heading" style="top:3405px">CONTACT</h2>
<svg class="abs divider" style="top:3456px" height="14" viewBox="0 0 40 14" fill="none" stroke="#2f87e2" stroke-width="2"><path d="M4 2l8 10M12 2L4 12M16 2l8 10M24 2l-8 10M28 2l8 10M36 2l-8 10"/></svg>

<div class="abs map" role="img" aria-label="Street map of the area with the studio location pin"></div>
<svg class="abs" style="left:572px;top:3690px" width="28" height="38" viewBox="0 0 28 38"><path d="M14 37S2 22 2 13a12 12 0 0 1 24 0c0 9-12 24-12 24z" fill="#e0334c"/><circle cx="14" cy="13" r="4.5" fill="#fff"/></svg>

<!-- footer -->
<footer class="abs footer"></footer>
<div class="abs social"><span></span><span></span><span></span><span></span><span></span></div>
<div class="abs copy script">© Copyright 2016. All rights reserved.</div>

<form class="abs form">
  <div class="field">Name</div>
  <div class="field">Email Address</div>
  <div class="field">Subject</div>
  <div class="field msg">Message</div>
  <div class="send">SEND</div>
</form>

</body>
</html>
```